依頼詳細
ウィッグオイルの商品パッケージデザインをお願いさせて頂きます。
ターゲットは10代後半〜30代前半の女性です。
可愛らしいデザインで女性の部屋においてある時に、馴染みやすいデザインにして頂けますと幸いです。

ウィッグオイルを使うことで、ウィッグがサラサラになり、ツヤが出るようなイメージが出来て、女性に気に入ってもらえるデザインがベストです。

ウィッグのツヤ出し、静電気防止、ウィッグの長持ち効果、柑橘系の香り、が商品の特徴的なポイントになります。

サイズ 100mm × サイズ150 mm
胴巻きラベルアート紙を使用します。

女性が主に使用しますので、普段使いの化粧品、美容品関係のようなシンプルながらも高級感のあるようなデザインが希望です。

```html
<!DOCTYPE html>
<html lang="ja">
<head>
<meta charset="UTF-8">
<title>Wig Oil ラベル</title>
<link rel="stylesheet" href="https://fonts.googleapis.com/css2?family=Marcellus&family=Noto+Sans+JP:wght@400;500&display=swap">
<style>
  :root {
    --pink: #ec7d90;
    --pink-text: #e8708a;
    --white: #ffffff;
    --lace-tone: #fbe6ea;
    --citrus: #ef7b86;
  }
  * { margin: 0; padding: 0; box-sizing: border-box; }
  html, body { width: 800px; height: 1200px; overflow: hidden; }
  body { background: var(--pink); font-family: "Noto Sans JP", sans-serif; }
  .label { position: relative; width: 800px; height: 1200px; background: var(--pink); }
  .medallion { position: absolute; left: 85px; top: 80px; width: 630px; height: 630px; }
  .medallion-text {
    position: absolute; left: 0; top: 0; width: 800px; text-align: center; color: var(--pink-text);
  }
  .scent {
    position: absolute; top: 294px; left: 0; width: 800px;
    display: flex; justify-content: center; align-items: center; gap: 10px;
    font-size: 27px; font-weight: 500; color: var(--pink-text);
  }
  .scent-icon { width: 30px; height: 30px; }
  .product-name {
    position: absolute; top: 330px; left: 0; width: 800px; text-align: center;
    font-family: "Marcellus", serif; font-size: 108px; line-height: 1.2; color: var(--pink-text);
    letter-spacing: 2px;
  }
  .texture {
    position: absolute; top: 472px; left: 0; width: 800px; text-align: center;
    font-size: 25px; line-height: 38px; color: var(--pink-text);
  }
  .benefit-band {
    position: absolute; left: 0; top: 795px; width: 800px; height: 125px; background: var(--white);
    display: flex; flex-direction: column; justify-content: center; align-items: center;
    color: var(--pink-text); font-size: 29px; line-height: 46px;
  }
  .net {
    position: absolute; top: 1058px; left: 0; width: 800px; text-align: center;
    color: var(--white); font-size: 33px; letter-spacing: 1px;
  }
</style>
</head>
<body>
<main class="label">
  <svg class="medallion" viewBox="0 0 630 630" xmlns="http://www.w3.org/2000/svg">
    <circle cx="315" cy="315" r="315" fill="var(--lace-tone)" role="img" aria-label="白いレース模様の円形飾り"/>
    <circle cx="315" cy="315" r="212" fill="var(--white)"/>
  </svg>
  <div class="scent">
    <svg class="scent-icon" viewBox="0 0 30 30" xmlns="http://www.w3.org/2000/svg">
      <circle cx="15" cy="17" r="12" fill="var(--citrus)"/>
      <path d="M15 5 q4 -4 8 -2 q-3 4 -8 2z" fill="var(--citrus)"/>
    </svg>
    <span>柑橘の香り</span>
  </div>
  <h1 class="product-name">Wig Oil</h1>
  <p class="texture">べとつかないサラサラ<br>スプレータイプ</p>
  <section class="benefit-band">
    <p>ウィッグのツヤ出し、静電気防止、</p>
    <p>ウィッグの長持ち効果に最適！</p>
  </section>
  <p class="net">NET 120ml</p>
</main>
</body>
</html>
```